Kestrel Hill Historic District Banner

Our Historic district is located in Allentown Pennsylvania, USA and is in need of a new banner design. The banners measure 18" wide by 36" tall. The banners are hung upon decorative street lights approximately 7' above ground. The district is adjacent to a downtown area that is experiencing significant growth and economic revitalization. The district is in need of a banner that respects the historic nature of the neighborhood while also saying that this is a hip urban residential neighborhood. You can visit our website at www.kestrelhill.org to learn more about our district. I also will upload our current logo which we like but think it may need some freshening up. I will also upload an image of one of the light poles.

just added a sketch of one thought that came up during one of my board meetings. We like the idea of keeping it simple, bold, easy to digest. we just upgraded many of our street signs in a black and white theme. thought it could be used in a playful positive and negative fashion. we also have previously liked color combinations of gold and blue - gold and black - gold and sepia - parchment and sepia

```html
<!DOCTYPE html>
<html lang="en">
<head>
<meta charset="utf-8">
<title>Kestrel Hill Historic District Banners</title>
<link rel="stylesheet" href="https://fonts.googleapis.com/css2?family=Cinzel:wght@600&family=Cormorant+Garamond:wght@600&display=swap">
<style>
  :root {
    --navy: #1b2a8c;
    --navy-deep: #121d66;
    --parchment: #f6f6f4;
    --gold-light: #f3d27a;
    --gold: #c9962f;
    --gold-dark: #8a5e12;
    --backdrop: #e9ebef;
  }
  html, body {
    margin: 0;
    padding: 0;
    overflow: hidden;
  }
  body {
    width: 1200px;
    height: 675px;
    background: var(--backdrop);
    display: flex;
    align-items: center;
    justify-content: center;
    gap: 70px;
  }
  .banner {
    width: 300px;
    height: 620px;
    display: block;
    filter: drop-shadow(0 6px 10px rgba(20, 30, 80, 0.18));
  }
  .name-mark {
    font-family: "Cinzel", serif;
    font-weight: 600;
    font-size: 42px;
    letter-spacing: 2px;
  }
  .district-caps {
    font-family: "Cinzel", serif;
    font-weight: 600;
    font-size: 36px;
    letter-spacing: 1px;
  }
  .district-script {
    font-family: "Cormorant Garamond", serif;
    font-weight: 600;
    font-size: 40px;
  }
  .fill-navy { fill: var(--navy); }
  .fill-paper { fill: var(--parchment); }
  .fill-gold { fill: url(#gold-sheen); }
</style>
</head>
<body>

<svg class="banner banner--navy-top" viewBox="0 0 300 620" aria-label="Kestrel Hill Historic District banner, navy over white">
  <defs>
    <linearGradient id="gold-sheen" x1="0" y1="0" x2="1" y2="1">
      <stop offset="0" stop-color="var(--gold-dark)"/>
      <stop offset="0.45" stop-color="var(--gold-light)"/>
      <stop offset="1" stop-color="var(--gold)"/>
    </linearGradient>
    <linearGradient id="rod-sheen" x1="0" y1="0" x2="0" y2="1">
      <stop offset="0" stop-color="var(--gold-light)"/>
      <stop offset="0.6" stop-color="var(--gold)"/>
      <stop offset="1" stop-color="var(--gold-dark)"/>
    </linearGradient>
  </defs>
  <rect class="fill-paper" x="0" y="30" width="300" height="560"/>
  <polygon class="fill-navy" points="0,30 300,30 300,160 0,550"/>
  <polygon class="fill-gold" points="300,160 300,182 0,572 0,550"/>
  <polygon class="fill-navy" points="300,188 300,192 0,582 0,578"/>
  <polygon class="fill-gold" points="0,30 46,30 0,84"/>
  <rect x="0" y="0" width="300" height="30" fill="url(#rod-sheen)"/>
  <rect x="0" y="590" width="300" height="30" fill="url(#rod-sheen)"/>
  <g transform="translate(118 300) rotate(-52.4)">
    <text class="name-mark" fill="var(--parchment)" text-anchor="middle" y="-10">KESTREL</text>
    <text class="name-mark" fill="var(--parchment)" text-anchor="middle" y="38">HILL</text>
  </g>
  <g transform="translate(212 450) rotate(-52.4)">
    <text class="district-caps" fill="var(--navy-deep)" text-anchor="middle" y="-8">HISTORIC</text>
    <text class="district-caps" fill="#2a2a2a" text-anchor="middle" y="32">DISTRICT</text>
  </g>
</svg>

<svg class="banner banner--white-top" viewBox="0 0 300 620" aria-label="Kestrel Hill Historic District banner, white over navy">
  <rect class="fill-paper" x="0" y="30" width="300" height="560"/>
  <polygon class="fill-navy" points="300,160 300,590 0,590 0,550"/>
  <polygon class="fill-gold" points="300,160 300,182 0,572 0,550"/>
  <polygon class="fill-navy" points="300,134 300,138 0,528 0,524"/>
  <polygon class="fill-gold" points="0,30 46,30 0,84"/>
  <rect x="0" y="0" width="300" height="30" fill="url(#rod-sheen)"/>
  <rect x="0" y="590" width="300" height="30" fill="url(#rod-sheen)"/>
  <g transform="translate(118 300) rotate(-52.4)">
    <text class="name-mark" fill="var(--navy)" text-anchor="middle" y="-10">KESTREL</text>
    <text class="name-mark" fill="var(--navy)" text-anchor="middle" y="38">HILL</text>
  </g>
  <g transform="translate(218 462) rotate(-52.4)">
    <text class="district-script" fill="var(--parchment)" text-anchor="middle" y="-8">Historic</text>
    <text class="district-script" fill="var(--parchment)" text-anchor="middle" y="30">District</text>
  </g>
</svg>

</body>
</html>
```